Chimney Service company needs new business card design

We need a updated business card with our new logo added. We provide a full range of chimney services throughout Vermont and New Hampshire. The business card will be one sided and color. Attached is our current business card another document showing all the information we would like on the card.
We dont like a lot of flashy colors.... here is a link to our website to get an idea of our branding www.flueguardianvt.example

Target Market(s)

homeowners

Industry/Entity Type

Business

Contact Information for Business Card

See attached sheet for content.

Font styles to use
Serif
Sans Serif

Requirements
Must have
• all information provided on separate sheet
Should not have
• Additional information that may clogg up design

```html
<!DOCTYPE html>
<html lang="en">
<head>
<meta charset="utf-8">
<title>Flue Guardian – Business Card</title>
<link rel="stylesheet" href="https://fonts.googleapis.com/css2?family=Cinzel:wght@600;700&family=Open+Sans:ital,wght@0,400;1,400;1,600&display=swap">
<style>
  :root {
    --backdrop: #1b1c1c;
    --card-white: #ffffff;
    --ink: #2b2b2b;
    --band-dark: #2e2e2e;
    --brand-red: #a11f22;
    --band-text: #d9d9d9;
  }
  * { margin: 0; padding: 0; box-sizing: border-box; }
  html, body {
    width: 1200px; height: 1000px; overflow: hidden;
    background: var(--backdrop);
  }
  .stage {
    width: 1200px; height: 1000px;
    display: flex; align-items: center; justify-content: center;
  }
  .business-card {
    position: relative;
    width: 900px; height: 514px;
    background: var(--card-white);
    border-radius: 26px;
    overflow: hidden;
    color: var(--ink);
  }
  .brand {
    position: absolute; left: 60px; top: 138px;
    width: 390px;
    display: flex; align-items: center; gap: 14px;
    white-space: nowrap;
  }
  .brand-square {
    flex: none;
    width: 36px; height: 36px; background: var(--brand-red);
  }
  .brand-name {
    font-family: "Cinzel", serif; font-weight: 700;
    font-size: 32px; letter-spacing: 1px; color: var(--ink);
  }
  .details {
    position: absolute; left: 500px; top: 70px;
    font-family: "Cinzel", serif; font-weight: 700;
    color: var(--ink);
    white-space: nowrap;
  }
  .details .pledge { font-size: 20px; line-height: 30px; }
  .details .contact { margin-top: 24px; font-size: 17px; line-height: 27px; }
  .rule {
    position: absolute; height: 6px; background: var(--brand-red);
  }
  .rule-left { left: 0; top: 262px; width: 330px; }
  .rule-right { right: 0; top: 290px; width: 230px; }
  .tagline {
    position: absolute; left: 346px; top: 254px;
    font-family: "Open Sans", sans-serif; font-style: italic; font-weight: 600;
    font-size: 21px; line-height: 30px; color: var(--ink);
    white-space: nowrap;
  }
  .service-band {
    position: absolute; left: 0; top: 304px; width: 100%; height: 142px;
    background: var(--band-dark);
    display: flex; justify-content: space-around; align-items: center;
    padding: 0 30px;
  }
  .service {
    font-family: "Open Sans", sans-serif; font-style: italic;
    font-size: 19px; line-height: 25px; text-align: center;
    color: var(--band-text);
  }
  .base-stripe {
    position: absolute; left: 0; top: 462px; width: 100%; height: 52px;
    background: var(--brand-red);
  }
</style>
</head>
<body>
<main class="stage">
  <article class="business-card">
    <div class="brand">
      <span class="brand-square"></span>
      <span class="brand-name">FLUE GUARDIAN</span>
    </div>

    <div class="details">
      <p class="pledge">Fully Insured – Free Estimate<br>Family owned and operated</p>
      <p class="contact">802-555-0147<br>info@flueguardianvt.example<br>www.flueguardianvt.example</p>
    </div>

    <div class="rule rule-left"></div>
    <p class="tagline">Serving VT and New Hampshire since 1989</p>
    <div class="rule rule-right"></div>

    <section class="service-band">
      <p class="service">Full Masonry<br>Services</p>
      <p class="service">Historic chimney<br>restoration</p>
      <p class="service">Stainless steel<br>liners</p>
      <p class="service">New Chimney<br>installations</p>
      <p class="service">Guild Certified<br>Chimney sweeps</p>
    </section>

    <div class="base-stripe"></div>
  </article>
</main>
</body>
</html>
```